Need a modern, bold, luxurious advertisement flyer for our roofing company. located in buffalo, ny. Big house with a intense roof design asphalt shingles. slogan is "Reliability starts at the top". Colors varies but want it to be modern. we will be handing these out when we are working in the area. phone number is 716-555-0143 for the TRUE PEAK estimate. also our services are roofing, roof repairs, gutters, attic ventilation. we offer a 15 year warranty with our summit shield plan. We are certified by dwellmatch, harlan pike, skarn. Also follow us on facebook, google and yelp. website is tpk-roofing.example, facebook is tpkroofing. pictures are on facebook and our website if need more can be provided. also can include a review we have.

```html
<!DOCTYPE html>
<html lang="en">
<head>
<meta charset="utf-8">
<title>TPK Roofing Flyer</title>
<link href="https://fonts.googleapis.com/css2?family=Open+Sans:wght@400;600;700;800&display=swap" rel="stylesheet">
<style>
:root{
  --orange:#e2640a;
  --orange-dark:#c9560a;
  --charcoal:#3c3c3c;
  --ink:#2b2b2b;
  --white:#ffffff;
  --page:#cfcfcf;
  --sky:#c9d8ea;
  --siding:#9aa0a4;
}
*{margin:0;padding:0;box-sizing:border-box}
html,body{width:1200px;height:1200px;overflow:hidden;background:var(--page);font-family:"Open Sans",sans-serif}
.flyer{position:absolute;left:225px;top:69px;width:936px;height:1326px;transform:scale(0.8);transform-origin:0 0;background:var(--white);overflow:hidden;color:var(--ink);box-shadow:0 20px 40px rgba(0,0,0,0.35)}
.abs{position:absolute}
.hero-photo{left:300px;top:0;width:636px;height:380px;background:linear-gradient(90deg,rgba(255,255,255,1) 0%,rgba(255,255,255,0) 35%),linear-gradient(180deg,var(--sky) 0%,#e8d9d6 45%,var(--siding) 100%)}
.shapes{left:0;top:0;width:936px;height:1326px}
.brand{left:84px;top:52px;display:flex;align-items:center;gap:14px}
.brand-square{width:44px;height:44px;background:var(--orange)}
.brand-name{font-size:64px;font-weight:800;color:var(--charcoal);letter-spacing:2px;line-height:1}
.tagline{left:36px;top:142px;font-size:19px;font-weight:700;color:var(--orange);letter-spacing:0.5px}
.company{left:42px;top:166px;font-size:31px;font-weight:400;color:var(--ink)}
.crew-photo{left:649px;top:284px;width:256px;height:256px;border-radius:50%;border:5px solid var(--orange);background:linear-gradient(135deg,#6d7b86,#b9bcbd 60%,#8a8f93)}
.slogan{left:43px;top:462px;font-size:30px;font-weight:800;color:var(--white);letter-spacing:0.3px}
.why{left:44px;top:526px;font-size:20px;font-weight:600;color:var(--orange)}
.about{left:44px;top:563px;width:693px;font-size:13.4px;line-height:19.4px;text-align:justify;color:var(--ink)}
.services-title{left:52px;top:690px;font-size:28px;font-weight:600;color:var(--ink)}
.services-title span{color:var(--orange)}
.services-rule{left:48px;top:730px;width:218px;height:3px;background:linear-gradient(90deg,var(--orange),rgba(226,100,10,0))}
.service-list{list-style:none;font-size:19px;color:var(--white);line-height:25.5px}
.service-list li{display:flex;align-items:center;gap:10px}
.tick{width:13px;height:13px;flex:none}
.col-a{left:58px;top:760px}
.col-b{left:308px;top:762px}
.warranty{right:30px;top:672px;text-align:right;line-height:1}
.warranty .lead{font-size:29px;font-weight:700;color:var(--charcoal)}
.warranty .big{font-size:51px;font-weight:800;color:var(--white);margin-top:5px;line-height:56px}
.warranty .tail{font-size:30px;font-weight:700;color:var(--charcoal);line-height:38px;margin-top:4px}
.job-photo{width:180px;height:180px;border-radius:50%;border:5px solid var(--orange);top:909px}
.job-a{left:93px;background:linear-gradient(160deg,#d9dde2,#9a9ca3 60%,#c9a7b5)}
.job-b{left:378px;background:linear-gradient(160deg,#7c8a7c,#e9ecef 45%,#9b6d45)}
.job-c{left:662px;background:linear-gradient(160deg,#c5c8c4,#7a6d5e 55%,#6f8654)}
.badge{top:1108px;height:29px;border-radius:15px;background:var(--charcoal);color:var(--white);font-size:22px;font-weight:700;line-height:29px;text-align:center}
.footer-band{left:0;top:1162px;width:936px;height:14px;background:var(--orange)}
.footer{left:0;top:1176px;width:936px;height:150px;background:var(--charcoal);color:var(--white)}
.footer h3{position:absolute;top:4px;font-size:21px;font-weight:600}
.footer p{position:absolute;font-size:19px;line-height:28px}
.divider{position:absolute;top:10px;width:2px;height:120px;background:var(--white)}
.social{position:absolute;top:59px;width:24px;height:24px;border-radius:50%;background:var(--white)}
</style>
</head>
<body>
<div class="flyer">
  <div class="abs hero-photo" role="img" aria-label="Photo of a large two-storey house with red and grey siding and a steep asphalt shingle roof"></div>

  <svg class="abs shapes" viewBox="0 0 936 1326" aria-hidden="true">
    <polygon points="0,209 369,372 710,230 936,230 936,425 229,434 0,361" fill="var(--orange)"/>
    <polygon points="369,372 710,230 936,230 936,290 229,434" fill="var(--orange-dark)" opacity="0.45"/>
    <polygon points="0,447 560,447 608,516 0,516" fill="var(--orange)"/>
    <polygon points="0,751 615,751 560,872 0,872" fill="var(--charcoal)"/>
    <polygon points="936,539 549,799 809,1162 936,1162" fill="var(--orange)"/>
    <polygon points="549,799 600,830 870,1162 809,1162" fill="var(--orange-dark)" opacity="0.5"/>
  </svg>

  <div class="abs brand"><span class="brand-square"></span><span class="brand-name">TPK</span></div>
  <div class="abs tagline">ROOFING-SIDING-STONE</div>
  <div class="abs company">ROOFING COMPANY</div>

  <div class="abs crew-photo" role="img" aria-label="Roofer in a company t-shirt installing a gutter, seen from behind"></div>

  <div class="abs slogan">RELIABILITY STARTS AT THE TOP</div>
  <div class="abs why">Why We’re the Right Choice for Your Roofing Needs</div>
  <p class="abs about">TPK Roofing has been serving the roofing needs of homeowners and commercial property owners throughout the greater Cedarview region since 2004. We specialize in roofing installation, repair, inspections, and re-roofs; gutter projects; and siding repair and installation. Our professionals help keep homes and commercial properties in tip top shape from the outside. If you are looking for a roofer to tackle your upcoming installation or unexpected repair job, choose the one that’s earned the title of Harlan Pike Preferred Contractor. Call us today for a quote and to discuss your project in detail.</p>

  <div class="abs services-title"><span>OUR</span> SERVICES</div>
  <div class="abs services-rule"></div>

  <ul class="abs service-list col-a">
    <li><svg class="tick" viewBox="0 0 14 14"><circle cx="7" cy="7" r="7" fill="var(--orange)"/><path d="M3.5 7.2l2.3 2.2 4.6-4.6" stroke="#fff" stroke-width="1.8" fill="none"/></svg>Roofing</li>
    <li><svg class="tick" viewBox="0 0 14 14"><circle cx="7" cy="7" r="7" fill="var(--orange)"/><path d="M3.5 7.2l2.3 2.2 4.6-4.6" stroke="#fff" stroke-width="1.8" fill="none"/></svg>Roof Repairs</li>
    <li><svg class="tick" viewBox="0 0 14 14"><circle cx="7" cy="7" r="7" fill="var(--orange)"/><path d="M3.5 7.2l2.3 2.2 4.6-4.6" stroke="#fff" stroke-width="1.8" fill="none"/></svg>Gutters</li>
    <li><svg class="tick" viewBox="0 0 14 14"><circle cx="7" cy="7" r="7" fill="var(--orange)"/><path d="M3.5 7.2l2.3 2.2 4.6-4.6" stroke="#fff" stroke-width="1.8" fill="none"/></svg>Attic Ventilation</li>
  </ul>
  <ul class="abs service-list col-b">
    <li><svg class="tick" viewBox="0 0 14 14"><circle cx="7" cy="7" r="7" fill="var(--orange)"/><path d="M3.5 7.2l2.3 2.2 4.6-4.6" stroke="#fff" stroke-width="1.8" fill="none"/></svg>Roof Installation</li>
    <li><svg class="tick" viewBox="0 0 14 14"><circle cx="7" cy="7" r="7" fill="var(--orange)"/><path d="M3.5 7.2l2.3 2.2 4.6-4.6" stroke="#fff" stroke-width="1.8" fill="none"/></svg>Commercial Roofing</li>
    <li><svg class="tick" viewBox="0 0 14 14"><circle cx="7" cy="7" r="7" fill="var(--orange)"/><path d="M3.5 7.2l2.3 2.2 4.6-4.6" stroke="#fff" stroke-width="1.8" fill="none"/></svg>Gutter</li>
    <li><svg class="tick" viewBox="0 0 14 14"><circle cx="7" cy="7" r="7" fill="var(--orange)"/><path d="M3.5 7.2l2.3 2.2 4.6-4.6" stroke="#fff" stroke-width="1.8" fill="none"/></svg>Siding Repair</li>
  </ul>

  <div class="abs warranty">
    <div class="lead">we offer a</div>
    <div class="big">15 year<br>warranty</div>
    <div class="tail">with our summit<br>shield plan</div>
  </div>

  <div class="abs job-photo job-a" role="img" aria-label="Roofer laying shingles on a snowy roof"></div>
  <div class="abs job-photo job-b" role="img" aria-label="Crew framing a new roof deck in winter"></div>
  <div class="abs job-photo job-c" role="img" aria-label="Company truck parked in front of a house"></div>

  <div class="abs badge" style="left:82px;width:200px">dwellmatch</div>
  <div class="abs badge" style="left:366px;width:204px">harlan pike</div>
  <div class="abs badge" style="left:661px;width:183px">skarn</div>

  <div class="abs footer-band"></div>
  <div class="abs footer">
    <h3 style="left:43px">Contact TPK Roofing</h3>
    <svg class="abs" style="left:50px;top:48px" width="18" height="18" viewBox="0 0 24 24"><path d="M6.6 10.8a15 15 0 006.6 6.6l2.2-2.2a1 1 0 011-.25 11.4 11.4 0 003.6.57 1 1 0 011 1V20a1 1 0 01-1 1A17 17 0 013 4a1 1 0 011-1h3.5a1 1 0 011 1 11.4 11.4 0 00.57 3.6 1 1 0 01-.25 1z" fill="var(--orange)"/></svg>
    <p style="left:82px;top:42px">716-555-0143</p>
    <svg class="abs" style="left:50px;top:75px" width="18" height="22" viewBox="0 0 24 30"><path d="M12 0a10 10 0 00-10 10c0 7.5 10 20 10 20s10-12.5 10-20A10 10 0 0012 0zm0 14a4 4 0 110-8 4 4 0 010 8z" fill="var(--orange)"/></svg>
    <p style="left:82px;top:70px">1820 Alder Ln, Cedarview,<br>NY 14000</p>
    <div class="divider" style="left:324px"></div>
    <h3 style="left:388px">Follow us:</h3>
    <span class="social" style="left:368px"></span>
    <span class="social" style="left:426px"></span>
    <span class="social" style="left:485px"></span>
    <div class="divider" style="left:556px"></div>
    <h3 style="left:580px">Hours of Operation</h3>
    <p style="left:580px;top:41px">Monday - Friday: 7 am to 6 pm<br>Saturday: 8 am to 3 pm<br>Sunday: By appointment</p>
  </div>
</div>
</body>
</html>
```